MS word document templates for consultancy

I need the following templates for my business using my logo as branding.

- General report template
- Letter head template
- Tender proposal template

The templates should be sleek and with minimal colors, but with a small amount of green and grey where appropriate (as per attached logo and email signature). Font should be consistent with the text in the email signature.

```html
<!DOCTYPE html>
<html lang="en">
<head>
<meta charset="utf-8">
<title>Keystride Group – Letterhead</title>
<link rel="stylesheet" href="https://fonts.googleapis.com/css2?family=Montserrat:wght@400;500&display=swap">
<style>
  :root {
    --backdrop: #eeeeee;
    --paper: #ffffff;
    --ink: #111111;
    --band-black: #000000;
    --brand-green: #3aa65a;
    --brand-green-dark: #248a42;
    --muted-text: #3c3c3c;
  }
  * { margin: 0; padding: 0; box-sizing: border-box; }
  html, body {
    width: 1200px;
    height: 721px;
    overflow: hidden;
    background: var(--backdrop);
  }
  .canvas {
    position: relative;
    width: 1200px;
    height: 721px;
  }
  .letterhead {
    position: absolute;
    left: 380px;
    top: 49px;
    width: 440px;
    height: 623px;
    background: var(--paper);
  }
  .letterhead svg { display: block; width: 100%; height: 100%; }
  .band-black { fill: var(--band-black); }
  .band-green { fill: var(--brand-green); }
  .band-green-dark { fill: var(--brand-green-dark); }
  .brand-name {
    font-family: "Montserrat", sans-serif;
    font-weight: 400;
    font-size: 22px;
    fill: var(--ink);
    letter-spacing: -0.3px;
  }
  .brand-sub {
    font-family: "Montserrat", sans-serif;
    font-weight: 400;
    font-size: 6px;
    fill: var(--ink);
  }
  .contact-text {
    font-family: "Montserrat", sans-serif;
    font-weight: 400;
    font-size: 7px;
    fill: var(--muted-text);
  }
  .contact-icon { fill: var(--brand-green); }
  .contact-glyph { fill: #ffffff; }
</style>
</head>
<body>
<main class="canvas">
  <section class="letterhead" aria-label="Keystride Group letterhead">
    <svg viewBox="0 0 466 660" xmlns="http://www.w3.org/2000/svg">
      <!-- header -->
      <g class="header-bands">
        <polygon class="band-black" points="0,0 326,0 343,31 258,31 240,8 0,8"/>
        <polygon class="band-green" points="343,17 389,17 396,31 350,31"/>
        <polygon class="band-green-dark" points="393,17 466,17 466,31 400,31"/>
      </g>
      <g class="brand">
        <text class="brand-name" x="18" y="37">Keystride</text>
        <text class="brand-sub" x="222" y="47" text-anchor="end">Group</text>
      </g>

      <!-- footer -->
      <g class="footer-bands">
        <polygon class="band-black" points="0,624 60,624 80,646 466,646 466,660 0,660"/>
        <polygon class="band-green" points="68,625 111,625 123,641 80,641"/>
        <polygon class="band-green" points="121,625 167,625 179,641 133,641"/>
      </g>

      <g class="contact contact-phone">
        <circle class="contact-icon" cx="240" cy="635" r="3.6"/>
        <path class="contact-glyph" d="M238.6,633.2 l0.9,-0.5 l0.7,1.2 l-0.5,0.4 q0.4,0.9 1.1,1.3 l0.4,-0.5 l1.2,0.7 l-0.5,0.9 q-2.6,-0.5 -3.3,-3.5z"/>
        <text class="contact-text" x="252" y="637.5">0412 305 644</text>
      </g>
      <g class="contact contact-email">
        <rect class="contact-icon" x="333.5" y="632" width="7" height="6" rx="2"/>
        <rect class="contact-glyph" x="335" y="633.6" width="4" height="2.8" rx="0.3"/>
        <text class="contact-text" x="345" y="637.5">alex@keystride.com</text>
      </g>
    </svg>
  </section>
</main>
</body>
</html>
```